Business Card for Dental Surgery

Professional and vibrant business card for dental surgery

Other side to incorporate space for appointment date and times

My website is www.larkvaledental.com.au

Target Market(s)

All

Industry/Entity Type

Dental

Requirements
Must have
• Catchy
Phone no, internet etc
Nice to have
• portray same image as website.
on reverse appointment side:
"Please give 24 hours notice if you cannot attend"
Nice colours

```html
<!DOCTYPE html>
<html lang="en">
<head>
<meta charset="utf-8">
<title>Larkvale Dental – Business Card</title>
<link rel="stylesheet" href="https://fonts.googleapis.com/css2?family=Arimo:wght@400;700&family=EB+Garamond&display=swap">
<style>
  :root {
    --backdrop: #e4e4e4;
    --card: #ffffff;
    --purple: #b22fd6;
    --purple-light: #d58be6;
    --purple-brand: #9b3aa0;
    --green: #0cb513;
    --green-light: #6fd873;
    --ink-grey: #6a6e75;
    --rule: #c9c9cf;
    --label: #333333;
  }
  * { margin: 0; padding: 0; box-sizing: border-box; }
  html, body { width: 1200px; height: 765px; overflow: hidden; }
  body {
    background: var(--backdrop);
    font-family: "Arimo", Arial, sans-serif;
    position: relative;
  }
  .card {
    position: absolute;
    top: 302px;
    width: 574px;
    height: 343px;
    background: var(--card);
    border-radius: 30px;
    overflow: hidden;
    box-shadow: 0 8px 14px rgba(0,0,0,0.28);
  }
  .card--front { left: 16px; }
  .card--back { left: 604px; }
  .card__band {
    position: absolute;
    left: 0; top: 0;
    width: 574px; height: 101px;
  }
  .card--front .card__band {
    background: linear-gradient(100deg, var(--purple) 0%, var(--purple) 18%, var(--purple-light) 42%, #c86fe0 70%, var(--purple-light) 100%);
  }
  .card--back .card__band {
    background: linear-gradient(100deg, var(--green) 0%, var(--green) 18%, var(--green-light) 42%, #34c63a 70%, var(--green-light) 100%);
  }
  .brand-name {
    position: absolute;
    font-weight: 700;
    color: var(--purple-brand);
    white-space: nowrap;
  }
  .card--front .brand-name { right: 20px; top: 238px; font-size: 33px; letter-spacing: -1px; }
  .card--back .brand-name { left: 67px; top: 202px; font-size: 22px; letter-spacing: -0.7px; }
  .website {
    position: absolute;
    left: 68px; top: 233px;
    font-size: 9.5px;
    letter-spacing: 1.6px;
    color: var(--purple-brand);
  }
  .notice {
    position: absolute;
    left: 0; right: 0; top: 72px;
    text-align: center;
    color: #ffffff;
    font-size: 17px;
  }
  .notice strong { font-weight: 700; }
  .appointment {
    position: absolute;
    left: 68px; top: 268px;
    width: 190px;
    font-size: 10px;
    color: var(--ink-grey);
  }
  .appointment__row {
    display: flex; align-items: flex-end;
    height: 20px;
  }
  .appointment__label { width: 34px; }
  .appointment__line { flex: 1; border-bottom: 1px solid var(--rule); height: 12px; }
  .contact {
    position: absolute;
    right: 69px; top: 169px;
    text-align: right;
    color: var(--ink-grey);
  }
  .contact__name { font-size: 33px; font-weight: 700; line-height: 1; letter-spacing: 0.5px; }
  .contact__title { font-size: 16px; margin-top: 1px; margin-bottom: 14px; }
  .contact__line {
    display: flex; justify-content: flex-end; align-items: center;
    font-size: 13.5px; letter-spacing: 0.6px; height: 15.5px;
  }
  .contact__line--email { font-size: 11px; letter-spacing: 0.2px; }
  .contact__line svg { width: 13px; height: 12px; margin-left: 15px; fill: var(--purple); flex: none; }
  .side-label {
    position: absolute;
    top: 686px;
    font-family: "EB Garamond", Georgia, serif;
    font-size: 14px;
    letter-spacing: 3px;
    color: var(--label);
  }
  .side-label--front { left: 66px; }
  .side-label--back { left: 659px; }
</style>
</head>
<body>

<section class="card card--front">
  <div class="card__band" role="img" aria-label="Soft purple header band with glossy light highlights"></div>
  <div class="brand-name">LarkvaleDental</div>
</section>

<section class="card card--back">
  <div class="card__band" role="img" aria-label="Soft green header band with glossy light highlights"></div>
  <p class="notice">Please give <strong>24 hours</strong> notice if you cannot attend</p>

  <div class="brand-name">LarkvaleDental</div>
  <div class="website">www.larkvaledental.com.au</div>

  <div class="appointment">
    <div class="appointment__row"><span class="appointment__label">Date</span><span class="appointment__line"></span></div>
    <div class="appointment__row"><span class="appointment__label">Time</span><span class="appointment__line"></span></div>
  </div>

  <div class="contact">
    <div class="contact__name">JOHN DOE</div>
    <div class="contact__title">Job Title</div>
    <div class="contact__line"><span>00 123 4567 890</span>
      <svg viewBox="0 0 13 12"><path d="M1 4 Q6.5 0 12 4 L10.5 5.5 L8.5 4.5 L8.5 3.5 Q6.5 3 4.5 3.5 L4.5 4.5 L2.5 5.5 Z M3 6 L10 6 L11.5 11 L1.5 11 Z"/></svg></div>
    <div class="contact__line"><span>00 123 4567 890</span>
      <svg viewBox="0 0 13 12"><rect x="3" y="0.5" width="7" height="3"/><rect x="0.5" y="4" width="12" height="5" rx="1"/><rect x="3" y="8" width="7" height="3.5"/></svg></div>
    <div class="contact__line"><span>00 123 4567 890</span>
      <svg viewBox="0 0 13 12"><rect x="1" y="3" width="11" height="8.5" rx="1"/><rect x="3" y="0.5" width="7" height="3"/><rect x="3" y="5" width="2" height="1.5" fill="#fff"/><rect x="6" y="5" width="2" height="1.5" fill="#fff"/><rect x="3" y="8" width="2" height="1.5" fill="#fff"/><rect x="6" y="8" width="2" height="1.5" fill="#fff"/></svg></div>
    <div class="contact__line contact__line--email"><span>john.doe@larkvaledental.com</span>
      <svg viewBox="0 0 13 12"><rect x="0.5" y="2" width="12" height="9" rx="1"/><path d="M1 2.5 L6.5 7 L12 2.5" stroke="#fff" stroke-width="1.2" fill="none"/></svg></div>
  </div>
</section>

<div class="side-label side-label--front">FRONT</div>
<div class="side-label side-label--back">BACK</div>

</body>
</html>
```